Website Redesign - We Need Your Magic!

Hello we are looking for you to help us re-design a high end and professional website for a high-end private school.

Here is the current site: http://www.brevanholt.example/

NOTE THIS IS DESIGN ONLY, NO CODING :)

The image they want to portray is that of high quality sports and education, in a creative "un-stiff" way.

Menu Bar: Horizontal

Look and Feel:

Site Colors: Dark green and a Gold yellow (logos are attached)

This site will represent a school so the look must be clean, bold, and classy. The site must have a very clean user interface, with things easily recognizable. Think simple.

The site should be visually appealing! If you come to me with templates, or a ton of text you will be out.

This site should be outside the box, we do not want boring, we do not want status quo. This site should instill excitement, innovation, and athletics.

So the main points again are:

1. High-end and classy look, with creative feel
2. Simple and clear navigation style
3. To cover the Junior and High School - Brevanholt College Schools

Think outside the box. We look forward to seeing what you come up with!!

Thank you for helping us create an amazing site for the school!

Industry/Entity Type

School

```html
<!DOCTYPE html>
<html lang="en">
<head>
<meta charset="utf-8">
<title>Brevanholt College</title>
<link rel="stylesheet" href="https://fonts.googleapis.com/css2?family=Montserrat:wght@400;700&family=Open+Sans:ital,wght@0,400;0,600;0,700;1,700&display=swap">
<style>
:root{
  --green:#0c5a34;
  --green-dark:#0a4a2b;
  --gold:#a8923a;
  --gold-text:#b89a2c;
  --yellow:#f5d400;
  --slate:#40444e;
  --navy:#1f2a44;
  --footer:#1d212a;
  --footer-bar:#111318;
  --ink:#2a2a2a;
  --muted:#6b6b6b;
  --white:#ffffff;
}
*{box-sizing:border-box;margin:0;padding:0}
html,body{width:1200px;height:900px;overflow:hidden;background:var(--white)}
body{font-family:"Open Sans",Arial,sans-serif;color:var(--ink);position:relative}
.head-font{font-family:"Montserrat",Arial,sans-serif}

/* header */
.site-header{position:absolute;top:0;left:0;width:1200px;height:42px;background:var(--white)}
.brand{position:absolute;left:0;width:1200px;top:10px;text-align:center;font-family:"Montserrat",Arial,sans-serif;font-weight:700;font-size:16px;color:var(--green);letter-spacing:1px}
.brand-mark{display:inline-block;width:12px;height:12px;background:var(--gold);margin-right:8px;vertical-align:-1px}

.main-nav{position:absolute;top:42px;left:0;width:1200px;height:18px;background:var(--gold);display:flex;justify-content:center;padding-left:10px}
.main-nav a{font-family:"Montserrat",Arial,sans-serif;font-size:9px;font-weight:700;color:var(--white);text-decoration:none;line-height:18px;padding:0 16px;letter-spacing:.5px}
.main-nav a.active{background:var(--green)}

/* hero */
.hero{position:absolute;top:60px;left:0;width:1200px;height:162px;background:linear-gradient(180deg,#c9d3da 0%,#8c8478 35%,#6f8a4a 62%,#5d7a3c 80%,#4a4840 100%)}
.hero-photo{position:absolute;inset:0}
.hero-arrow{position:absolute;top:50px}
.hero-arrow.prev{left:14px}
.hero-arrow.next{right:10px}
.hero-copy{position:absolute;left:662px;top:12px;width:440px}
.hero-kicker{font-family:"Montserrat",Arial,sans-serif;font-size:11px;color:#e6e6e6;letter-spacing:1px}
.hero-title{font-family:"Montserrat",Arial,sans-serif;font-weight:700;font-size:20px;line-height:20px;color:var(--yellow);letter-spacing:1px;margin-top:3px}
.hero-text{font-size:12px;line-height:13px;color:#eeeeee;margin-top:4px;width:380px}
.btn-detail{position:absolute;left:0;top:113px;width:162px;height:18px;background:var(--green);color:var(--white);font-family:"Montserrat",Arial,sans-serif;font-size:10px;text-align:center;line-height:18px;letter-spacing:1px}

/* welcome */
.welcome{position:absolute;top:222px;left:0;width:1200px;height:156px}
.welcome-copy{position:absolute;left:167px;top:27px;width:420px}
.section-title{font-family:"Montserrat",Arial,sans-serif;font-weight:700;font-size:16px;color:var(--green);letter-spacing:1px}
.lead{font-weight:700;font-size:10px;line-height:10px;color:#333;margin-top:5px}
.body-text{font-size:9.5px;line-height:10.5px;color:var(--muted);margin-top:5px}
.welcome-text{height:42px;overflow:hidden}
.btn-more{position:absolute;left:0;top:95px;width:126px;height:13px;background:var(--navy);color:#c9cbd2;font-size:7px;line-height:13px;padding-left:20px}
.welcome-photo{position:absolute;left:610px;top:29px;width:426px;height:105px;background:linear-gradient(180deg,#8a8a86 0%,#5d6a5a 45%,#6f8a3a 90%)}

/* features */
.features{position:absolute;top:378px;left:0;width:1200px;height:260px;background:var(--slate)}
.feature-card{position:absolute;width:425px;height:98px;background:var(--white);display:flex}
.feature-photo{width:148px;height:98px;flex:none}
.feature-body{padding:10px 20px}
.feature-title{font-family:"Montserrat",Arial,sans-serif;font-weight:700;font-size:11px;color:var(--gold-text);letter-spacing:1px}
.feature-text{font-size:8px;line-height:9.5px;color:var(--muted);margin-top:6px;width:240px}
.feature-link{font-size:8px;color:var(--muted);margin-top:8px}

/* about */
.about{position:absolute;top:638px;left:0;width:1200px;height:154px}
.about-copy{position:absolute;left:166px;top:27px;width:420px}
.about-title{font-family:"Montserrat",Arial,sans-serif;font-weight:700;font-size:15px;line-height:13px;color:var(--green);letter-spacing:.5px;padding-bottom:7px;border-bottom:1px solid #dcdcdc}
.about-lead{font-style:italic;font-weight:700;font-size:10px;line-height:10.5px;color:#333;margin-top:5px;text-align:justify}
.about-text{font-size:9.5px;line-height:10.5px;color:var(--muted);margin-top:6px}
.bullet-list{position:absolute;top:28px;width:185px;list-style:none}
.bullet-list li{font-size:10px;line-height:11px;color:#444;padding-left:26px;position:relative}
.bullet-list li::before{content:"";position:absolute;left:0;top:4px;width:5px;height:5px;background:#444}
.bullet-list li.cont::before{display:none}

/* footer */
.site-footer{position:absolute;top:792px;left:0;width:1200px;height:90px;background:var(--footer)}
.footer-col{position:absolute;top:9px}
.footer-head{font-family:"Montserrat",Arial,sans-serif;font-weight:700;font-size:7.5px;color:var(--gold-text);letter-spacing:1px;margin-bottom:6px}
.footer-links{list-style:none}
.footer-links li{font-size:7.5px;line-height:8px;color:#c8c8c8}
.footer-small{font-size:6.5px;line-height:7px;color:#9a9ca3}
.footer-meta{font-size:6px;color:#c8c8c8;font-style:italic;margin:2px 0 7px}
.footer-more{font-size:7px;color:#d0d0d0;text-decoration:underline}
.contact-line{display:flex;align-items:center;gap:8px;font-size:6.5px;color:#9a9ca3;margin-top:3px}
.date-box{position:absolute;left:0;width:70px;height:21px;background:#0e1014;text-align:center;color:#ddd}
.date-day{font-size:12px;line-height:13px}
.date-month{font-size:5.5px;line-height:7px}
.testimonial{position:absolute;left:90px;width:170px}
.pager{position:absolute;left:210px;top:72px;display:flex;gap:3px}
.pager span{width:16px;height:8px;background:#0e1014;display:flex;align-items:center;justify-content:center}

.footer-bar{position:absolute;top:882px;left:0;width:1200px;height:18px;background:var(--footer-bar)}
.copyright{position:absolute;left:168px;top:4px;font-size:6.5px;color:#bbbbbb}
.social{position:absolute;left:940px;top:3px;display:flex;gap:6px}
.social span{width:26px;height:12px;border-radius:6px;background:#5a5d64}
</style>
</head>
<body>

<header class="site-header">
  <div class="brand"><span class="brand-mark"></span>Brevanholt College</div>
</header>

<nav class="main-nav">
  <a href="#" class="active">HOME</a>
  <a href="#">ABOUT</a>
  <a href="#">ACADEMICS</a>
  <a href="#">SPORTS</a>
  <a href="#">JOINING BREVANHOLT</a>
  <a href="#">CONTACT</a>
</nav>

<section class="hero">
  <div class="hero-photo" role="img" aria-label="Students relaxing on a college lawn in front of historic stone buildings"></div>
  <svg class="hero-arrow prev" width="24" height="28" viewBox="0 0 24 28"><polyline points="20,2 6,14 20,26" fill="none" stroke="#ffffff" stroke-width="2"/></svg>
  <svg class="hero-arrow next" width="24" height="28" viewBox="0 0 24 28"><polyline points="4,2 18,14 4,26" fill="none" stroke="#ffffff" stroke-width="2"/></svg>
  <div class="hero-copy">
    <div class="hero-kicker">LOREM IPSUM DOLOR</div>
    <h1 class="hero-title">LOREM IPSUME<br>DOLOR SIT IS LOREM</h1>
    <p class="hero-text">Lorem ipsume dolor sit is lorem ipsume dolor sit dummy text</p>
    <div class="btn-detail">VIEW DETAIL</div>
  </div>
</section>

<section class="welcome">
  <div class="welcome-copy">
    <h2 class="section-title">WELCOME TO OUR COLLEGE</h2>
    <p class="lead">Lorem Ipsum is simply dummy text of the printing and typesetting industry Lorem</p>
    <p class="body-text welcome-text">Lorem Ipsum is simply dummy text of the printing and type-setting industry. Lorem Ipsum has been the industry's standard dummy text ever since. Lorem Ipsum is simply dummy text of the printing and typesetting industry. Lorem Ipsum has been the industry's standard dummy text ever since. Lorem Ipsum is simply dummy text of the printing and</p>
    <div class="btn-more">Read More [+]</div>
  </div>
  <div class="welcome-photo" role="img" aria-label="Students with backpacks walking across the campus"></div>
</section>

<section class="features">
  <article class="feature-card" style="left:166px;top:27px">
    <div class="feature-photo" role="img" aria-label="Hockey players on a pitch" style="background:linear-gradient(180deg,#6f8f6a,#5fb7a6 60%,#3c8c7e)"></div>
    <div class="feature-body">
      <h3 class="feature-title">HEADING GOES HERE</h3>
      <p class="feature-text">Lorem Ipsum is simply dummy text of the printing and typesetting industry. Lorem Ipsum has been the industry's standard dummy text ever since the 1500s,</p>
      <p class="feature-link">[ Read More ]</p>
    </div>
  </article>
  <article class="feature-card" style="left:610px;top:27px">
    <div class="feature-photo" role="img" aria-label="Students studying together at a laptop" style="background:linear-gradient(180deg,#3a2c28,#7a5a48 55%,#4a6fa0)"></div>
    <div class="feature-body">
      <h3 class="feature-title">HEADING GOES HERE</h3>
      <p class="feature-text">Lorem Ipsum is simply dummy text of the printing and typesetting industry. Lorem Ipsum has been the industry's standard dummy text ever since the 1500s,</p>
      <p class="feature-link">[ Read More ]</p>
    </div>
  </article>
  <article class="feature-card" style="left:166px;top:134px">
    <div class="feature-photo" role="img" aria-label="Indoor football players in a sports hall" style="background:linear-gradient(180deg,#8a8f7a,#c8b070 55%,#d8c48a)"></div>
    <div class="feature-body">
      <h3 class="feature-title">HEADING GOES HERE</h3>
      <p class="feature-text">Lorem Ipsum is simply dummy text of the printing and typesetting industry. Lorem Ipsum has been the industry's standard dummy text ever since the 1500s,</p>
      <p class="feature-link">[ Read More ]</p>
    </div>
  </article>
  <article class="feature-card" style="left:610px;top:134px">
    <div class="feature-photo" role="img" aria-label="Student reading a book" style="background:linear-gradient(180deg,#d8d6d2,#5a3a30 50%,#1f2a44)"></div>
    <div class="feature-body">
      <h3 class="feature-title">HEADING GOES HERE</h3>
      <p class="feature-text">Lorem Ipsum is simply dummy text of the printing and typesetting industry. Lorem Ipsum has been the industry's standard dummy text ever since the 1500s,</p>
      <p class="feature-link">[ Read More ]</p>
    </div>
  </article>
</section>

<section class="about">
  <div class="about-copy">
    <h2 class="about-title">Lorem Ipsum is simply dummy<br>text of the printing</h2>
    <p class="about-lead">Lorem Ipsum is simply dummy text of the printing and typesetting industry Lorem Ipsum has been</p>
    <p class="about-text">Lorem Ipsum is simply dummy text of the printing and typesetting industry Lorem Ipsum has been the industry's standard dummy text ever since</p>
  </div>
  <ul class="bullet-list" style="left:610px">
    <li>Lorem Ipsum is simply</li><li>dummy text of the</li><li>printing and</li><li>typesetting industry</li><li>Lorem Ipsum has</li><li>been the industry's</li><li>standard dummy text</li><li>ever since the 1500s,</li><li>when an unknown</li>
  </ul>
  <ul class="bullet-list" style="left:836px">
    <li>Lorem Ipsum is simply</li><li>dummy text of the</li><li>printing and</li><li>typesetting industry</li><li>Lorem Ipsum has</li><li>been the industry's</li><li>standard dummy text</li><li>ever since the 1500s,</li><li>when an unknown</li>
  </ul>
</section>

<footer class="site-footer">
  <div class="footer-col" style="left:168px">
    <div class="footer-head">QUICK LINK</div>
    <ul class="footer-links">
      <li>Home</li><li>About</li><li>Academics</li><li>Sports</li><li>At Working</li><li>Contact</li>
    </ul>
  </div>
  <div class="footer-col" style="left:315px;width:150px">
    <div class="footer-head">BLOG</div>
    <p class="footer-small">Lorem Ipsum has been the industry's standard dummy text</p>
    <p class="footer-meta">- Mara Keld &nbsp;&nbsp; 15 Dec 2013</p>
    <p class="footer-small">Lorem Ipsum has been the industry's standard dummy text</p>
    <p class="footer-meta">- Mara Keld &nbsp;&nbsp; 15 Dec 2013</p>
    <span class="footer-more">View More</span>
  </div>
  <div class="footer-col" style="left:540px;width:150px">
    <div class="footer-head">ADDRESS</div>
    <p class="footer-small">Lorem Ipsum has been the industry's standard dummy text</p>
    <div class="contact-line" style="margin-top:8px">
      <svg width="9" height="8" viewBox="0 0 9 8"><path d="M1 1 Q1 7 8 7 L8 5 L6 4.5 L5 5.5 Q3 4.5 2.5 3 L3.5 2 L3 0 Z" fill="#ffffff"/></svg>0100 2000
    </div>
    <div class="contact-line">
      <svg width="9" height="7" viewBox="0 0 9 7"><rect x="0.5" y="0.5" width="8" height="6" fill="#ffffff"/><polyline points="0.5,0.5 4.5,4 8.5,0.5" fill="none" stroke="#1d212a" stroke-width="0.8"/></svg>office@brevanholt.example
    </div>
  </div>
  <div class="footer-col" style="left:756px;width:280px;height:80px">
    <div class="footer-head">TESTIMONIALS</div>
    <div class="date-box" style="top:16px"><div class="date-day">15</div><div class="date-month">March 2014</div></div>
    <div class="testimonial" style="top:20px"><p class="footer-small">Lorem Ipsum has been the industry's standard dummy text</p><p class="footer-meta">- Mara Keld</p></div>
    <div class="date-box" style="top:42px"><div class="date-day">18</div><div class="date-month">March 2014</div></div>
    <div class="testimonial" style="top:46px"><p class="footer-small">Lorem Ipsum has been the industry's standard dummy text</p><p class="footer-meta">- Mara Keld</p></div>
    <div class="pager">
      <span><svg width="8" height="5" viewBox="0 0 8 5"><polygon points="0,2.5 3,0 3,5" fill="#fff"/><rect x="3" y="2" width="5" height="1" fill="#fff"/></svg></span>
      <span><svg width="8" height="5" viewBox="0 0 8 5"><polygon points="8,2.5 5,0 5,5" fill="#fff"/><rect x="0" y="2" width="5" height="1" fill="#fff"/></svg></span>
    </div>
  </div>
</footer>

<div class="footer-bar">
  <p class="copyright">Design©2014. All Rights Reserved.</p>
  <div class="social"><span></span><span></span><span></span></div>
</div>

</body>
</html>
```